New Wordpress Website

We need a new wordpress website for our IT Association. Our main corporate colour is orange. Style Guideline attached.
The association is an NFP for IT Professionals. An opportunity for our members to collaborate and grow as a community.

Current website can be found at: www.lumentechguild.org

Target Market(s)

IT Professionals and Small Business Owners who need IT Information

Industry/Entity Type

Information Technology

Coding

Colors
f37122

```html
<!DOCTYPE html>
<html lang="en">
<head>
<meta charset="utf-8">
<title>Lumen Tech Guild – Home Page, Light and Dark Themes</title>
<link rel="stylesheet" href="https://fonts.googleapis.com/css2?family=Roboto:ital,wght@0,400;0,500;0,700;0,900;1,400&display=swap">
<style>
  :root{
    --orange:#ee5b1e;
    --stage:#8a8a8a;
    --ink:#2f2f2f;
    --muted:#777;
  }
  *{box-sizing:border-box;margin:0;padding:0}
  html,body{width:819px;height:1200px;overflow:hidden}
  body{background:var(--stage);font-family:'Roboto',Arial,sans-serif;position:relative}

  .page{position:absolute;top:57px;width:352px;height:1086px;overflow:hidden;background:var(--bg)}
  .page--light{left:39px;--bg:#ffffff;--alt:#f6f6f6;--head:#ffffff;--title:#2f2f2f;--text:#7a7a7a;--nav:#333;--card:#ffffff;--line:#e3e3e3;--swoosh:#2f2f2f}
  .page--dark{left:429px;--bg:#2f2f2f;--alt:#2a2a2a;--head:#333333;--title:#ffffff;--text:#d6d6d6;--nav:#ffffff;--card:#ffffff;--line:#555;--swoosh:#3c3c3c}

  .abs{position:absolute}

  /* header */
  .header{left:0;top:0;width:352px;height:35px;background:var(--head)}
  .callbar{right:0;top:0;height:12px;width:140px;background:var(--orange);clip-path:polygon(8% 0,100% 0,100% 100%,14% 100%);color:#fff;font-size:5.2px;font-weight:700;display:flex;align-items:center;justify-content:center;gap:3px}
  .callbar svg{width:7px;height:7px}
  .nav{left:132px;top:21px;display:flex;gap:8px;font-size:3.8px;font-weight:700;color:var(--nav);letter-spacing:.1px}
  .nav .active{color:var(--orange)}
  .brand{left:41px;top:-6px;width:62px;height:62px;border-radius:50%;background:var(--head);display:flex;flex-direction:column;align-items:center;justify-content:center;z-index:3;text-align:center}
  .brand-dot{width:9px;height:9px;border-radius:50%;border:1.6px solid var(--orange);margin-bottom:2px}
  .brand-name{font-size:6.4px;font-weight:700;color:var(--title);line-height:1.05}

  /* hero */
  .hero-photo{left:0;top:35px;width:352px;height:205px;background:linear-gradient(100deg,#b9c0c4 0%,#8f989c 35%,#55606a 62%,#2e3640 100%)}
  .hero-title{left:42px;top:84px;font-size:23px;font-weight:900;line-height:1;color:#fff;letter-spacing:.3px}
  .hero-title span{color:var(--orange)}
  .hero-sub{left:42px;top:143px;font-size:6px;font-weight:700;color:#fff}
  .btns{left:42px;top:164px;display:flex;gap:3px}
  .btn{height:13px;padding:0 5px;display:flex;align-items:center;gap:4px;font-size:3.8px;font-weight:700;color:#fff;background:var(--orange)}
  .btn--dark{background:#2f2f2f}
  .btn svg{width:6px;height:6px}
  .dots{left:42px;top:196px;display:flex;gap:2px}
  .dots i{width:2.4px;height:2.4px;border-radius:50%;background:#fff}
  .dots i.on{background:var(--orange)}
  .side{right:0;display:flex;align-items:center;justify-content:flex-end}
  .side-tab{height:11px;width:20px;background:var(--orange);border-radius:6px 0 0 6px;display:flex;align-items:center;padding-left:2px}
  .side-tab b{width:7px;height:7px;border-radius:50%;background:#fff;display:block}
  .side-join{height:11px;background:#fff;border-radius:6px 0 0 6px;display:flex;align-items:center;gap:3px;padding:0 4px 0 2px;font-size:3.2px;font-weight:700;color:#333}
  .side-join b{width:7px;height:7px;border-radius:50%;background:var(--orange);display:block}
  .hero-wave{left:0;top:205px;width:352px;height:45px}
  .mark{left:166px;top:212px;width:20px;height:20px;border-radius:50%;background:var(--bg);display:flex;align-items:center;justify-content:center;z-index:2}
  .mark i{width:11px;height:11px;border-radius:50%;border:2px solid var(--orange);display:block}

  /* intro */
  .center{left:0;width:352px;text-align:center}
  .h2{font-size:10.5px;font-weight:500;color:var(--title);line-height:1.38}
  .h2 em{font-style:normal;color:var(--orange)}
  .intro{top:300px;left:66px;width:220px;font-size:3.7px;line-height:8.7px;color:var(--text);text-align:center}
  .intro p+p{margin-top:3px}

  .alt-band{left:0;top:400px;width:352px;height:370px;background:var(--alt)}
  .swoosh{left:0;top:400px;width:352px;height:330px}
  .pillar{border-radius:50%;border:3px solid var(--orange);background:#3e3a39;color:#fff;text-align:center;display:flex;flex-direction:column;align-items:center;justify-content:center;padding:0 10px;box-shadow:0 3px 5px rgba(0,0,0,.25)}
  .pillar--main{border:5px solid var(--orange);box-shadow:0 0 0 1px #fff inset,0 6px 8px rgba(0,0,0,.25)}
  .page--dark .pillar--main{border-color:#4a4a4a;box-shadow:0 0 0 1px #fff inset}
  .pillar svg{width:18px;height:18px;margin-bottom:2px}
  .pillar h3{font-size:7.5px;font-weight:500;margin-bottom:3px}
  .pillar p{font-size:3.2px;line-height:5.4px}

  .find-btn{left:155px;top:519px;width:42px;height:12px;justify-content:center}
  .video{left:71px;top:552px;width:209px;height:117px;background:linear-gradient(90deg,#a9b0a8 0%,#6f7570 35%,#34373d 60%,#8c8880 100%);border:1px solid #fff}
  .play{left:167px;top:601px;width:18px;height:18px}

  .logos{left:30px;top:728px;width:292px;display:flex;align-items:center;gap:6px}
  .arrow{width:9px;height:9px;border-radius:50%;border:.6px solid #bbb;display:flex;align-items:center;justify-content:center;font-size:5px;color:#999;flex:none}
  .badge{width:48px;height:25px;background:var(--card);border:.6px solid var(--line);display:flex;align-items:center;justify-content:center;flex:none}
  .badge i{width:26px;height:7px;border-radius:2px;background:#d8dce2;display:block}
  .logos .arrow:first-child{margin-right:6px}
  .logos .arrow:last-child{margin-left:6px}

  /* testimonials */
  .orange-wave{left:0;top:765px;width:352px;height:220px}
  .testi-title{top:836px;font-size:10.5px;font-weight:500;color:#fff}
  .testi-title span{color:var(--title)}
  .page--dark .testi-title span{color:#2f2f2f}
  .quote{left:147px;top:870px;width:155px;font-size:3.6px;line-height:8px;font-style:italic;color:#fff}
  .cite{left:147px;top:900px;font-size:3.6px;line-height:6.5px;font-weight:700;color:#fff}
  .testi-nav{left:147px;top:923px;display:flex;gap:3px}
  .testi-nav span{width:9px;height:9px;border-radius:50%;border:.6px solid #fff;color:#fff;font-size:5px;display:flex;align-items:center;justify-content:center}
  .portrait{left:48px;top:884px;width:68px;height:84px;background:linear-gradient(180deg,#d7a98a 0%,#2b2f3a 45%,#1f232c 100%);border-radius:34px 34px 0 0}
  .mark--foot{top:969px}

  /* footer */
  .foot-brand{left:42px;top:988px;width:50px;text-align:center}
  .foot-brand .brand-dot{width:16px;height:16px;border-width:2.4px;margin:0 auto 4px}
  .foot-brand .brand-name{font-size:7px}
  .social{left:42px;top:1042px;display:flex;gap:3px}
  .social i{width:5px;height:5px;background:var(--orange);border-radius:1px;display:block}
  .foot-h{font-size:6px;font-weight:500;color:var(--title)}
  .links{left:118px;top:1010px;display:grid;grid-template-columns:35px 35px;font-size:3.6px;line-height:7.8px;color:var(--text)}
  .join-text{left:200px;top:1011px;font-size:3.6px;color:var(--text)}
  .signup{left:200px;top:1025px;width:108px;height:13px;border-radius:7px;background:#fff;border:.6px solid #ddd;display:flex;align-items:center;justify-content:space-between;padding-left:7px;font-size:3.6px;color:#555}
  .signup b{height:100%;width:31px;border-radius:7px;background:var(--orange);color:#fff;font-size:3.8px;display:flex;align-items:center;justify-content:center}
  .foot-rule{left:42px;top:1063px;width:268px;height:.6px;background:var(--line)}
  .copy{top:1072px;font-size:3.6px;color:var(--text)}
</style>
</head>
<body>

<!-- ===== Light theme ===== -->
<section class="page page--light">
  <div class="abs header"></div>
  <div class="abs callbar"><svg viewBox="0 0 10 10"><circle cx="5" cy="5" r="4.3" fill="none" stroke="#fff" stroke-width=".8"/><path d="M3.4 2.8l1 .9-.5.7a3 3 0 0 0 1.7 1.7l.7-.5.9 1-.6.7C4.6 7.1 2.9 5.4 2.7 3.4z" fill="#fff"/></svg>CALL US : 1 800 555 0199</div>
  <nav class="abs nav"><span>HOME</span><span>HOW IT WORKS</span><span>JOIN</span><span>CHAPTERS</span><span>MEMBERS</span><span>PARTNERS</span><span>MORE</span></nav>
  <div class="abs brand"><span class="brand-dot"></span><span class="brand-name">LUMEN<br>TECH GUILD</span></div>

  <div class="abs hero-photo" role="img" aria-label="Smiling young professional in a suit in a bright office"></div>
  <h1 class="abs hero-title">STRENGTH<br>IN <span>NUMBERS</span></h1>
  <p class="abs hero-sub">Sed ut perspiciatis unde omnis iste natus voluptatem</p>
  <div class="abs btns">
    <span class="btn">JOIN US <svg viewBox="0 0 10 10"><circle cx="5" cy="5" r="4.2" fill="none" stroke="#fff" stroke-width=".8"/><path d="M3 5h4M5.4 3.4 7 5 5.4 6.6" fill="none" stroke="#fff" stroke-width=".8"/></svg></span>
    <span class="btn btn--dark">DOWNLOAD BROCHURE <svg viewBox="0 0 10 10"><circle cx="5" cy="5" r="4.2" fill="none" stroke="#fff" stroke-width=".8"/><path d="M3 5h4M5.4 3.4 7 5 5.4 6.6" fill="none" stroke="#fff" stroke-width=".8"/></svg></span>
  </div>
  <div class="abs dots"><i></i><i></i><i class="on"></i><i></i><i></i></div>
  <div class="abs side" style="top:112px"><span class="side-tab"><b></b></span></div>
  <div class="abs side" style="top:127px"><span class="side-join"><b></b>JOIN US</span></div>
  <div class="abs side" style="top:143px"><span class="side-tab"><b></b></span></div>
  <svg class="abs hero-wave" viewBox="0 0 352 45" preserveAspectRatio="none">
    <path d="M0 27 Q170 40 352 14 L352 45 L0 45Z" fill="var(--bg)"/>
    <path d="M0 26 Q120 44 250 24" fill="none" stroke="var(--orange)" stroke-width="4"/>
    <path d="M190 16 Q290 6 352 20" fill="none" stroke="#2f2f2f" stroke-width="4"/>
  </svg>
  <div class="abs mark"><i></i></div>

  <h2 class="abs center h2" style="top:263px">GROW YOUR BUSINESS,<br><em>GROW YOUR REPUTATION</em></h2>
  <div class="abs intro">
    <p>Lumen Tech Guild is Australia's leading industry association for IT business owners and professionals specialising in IT solutions for small and medium business.</p>
    <p>As a Lumen Tech Guild member you can draw upon, and add to, the collective knowledge bank of best-practice solutions and expert opinions garnered from a national network of IT business owners and professionals.</p>
  </div>

  <div class="abs alt-band"></div>
  <svg class="abs swoosh" viewBox="0 0 352 330" preserveAspectRatio="none">
    <path d="M300 75 Q330 62 352 55 L352 61 Q330 68 300 80Z" fill="var(--orange)"/>
    <path d="M0 280 Q20 268 71 258 L71 262 Q25 272 0 287Z" fill="var(--swoosh)"/>
  </svg>
  <div class="abs pillar" style="left:48px;top:364px;width:82px;height:82px">
    <svg viewBox="0 0 20 20" fill="none" stroke="#fff" stroke-width="1"><circle cx="8" cy="8" r="5.5"/><path d="M12 12l5 5"/></svg>
    <h3>Seek</h3><p>Liberate your time and find proven IT solutions fast via the Lumen Tech Guild Forum.</p>
  </div>
  <div class="abs pillar pillar--main" style="left:126px;top:356px;width:100px;height:100px">
    <svg viewBox="0 0 20 20" fill="none" stroke="#fff" stroke-width="1"><path d="M4 6h4a2 2 0 1 1 4 0h4v4a2 2 0 1 0 0 4v3H4v-3a2 2 0 1 0 0-4z"/></svg>
    <h3>Solve</h3><p>Create a more efficient and effective business, and deliver greater value to your customers via fast, effective problem-solving.</p>
  </div>
  <div class="abs pillar" style="left:222px;top:364px;width:82px;height:82px">
    <svg viewBox="0 0 20 20" fill="none" stroke="#fff" stroke-width=".9"><rect x="7" y="7" width="6" height="6"/><circle cx="10" cy="2.5" r="1.3"/><circle cx="10" cy="17.5" r="1.3"/><circle cx="2.5" cy="10" r="1.3"/><circle cx="17.5" cy="10" r="1.3"/><path d="M10 4v3M10 13v3M4 10h3M13 10h3"/></svg>
    <h3>Share</h3><p>Join the collective buying power and influence of Australia's largest industry association for small &amp; medium business IT.</p>
  </div>

  <h2 class="abs center h2" style="top:482px">FIND YOUR LOCAL<br><em>LUMEN TECH GUILD CHAPTER.</em></h2>
  <span class="abs btn find-btn">FIND NOW <svg viewBox="0 0 10 10"><circle cx="5" cy="5" r="4.2" fill="none" stroke="#fff" stroke-width=".8"/><path d="M3 5h4M5.4 3.4 7 5 5.4 6.6" fill="none" stroke="#fff" stroke-width=".8"/></svg></span>
  <div class="abs video" role="img" aria-label="Video still of a presenter speaking on a city street"></div>
  <svg class="abs play" viewBox="0 0 20 20"><circle cx="10" cy="10" r="9" fill="rgba(0,0,0,.35)" stroke="#fff" stroke-width="1"/><path d="M8 6l6 4-6 4z" fill="#fff"/></svg>

  <h2 class="abs center h2" style="top:698px">KEY <em>PARTNERS</em></h2>
  <div class="abs logos">
    <span class="arrow">‹</span>
    <span class="badge"><i></i></span><span class="badge"><i></i></span><span class="badge"><i></i></span><span class="badge"><i></i></span><span class="badge"><i></i></span>
    <span class="arrow">›</span>
  </div>

  <svg class="abs orange-wave" viewBox="0 0 352 220" preserveAspectRatio="none">
    <path d="M0 28 Q90 36 170 30 Q270 16 352 20 L352 204 Q250 170 170 186 Q80 206 0 196Z" fill="var(--orange)"/>
    <path d="M0 26 Q50 40 130 38" fill="none" stroke="#2f2f2f" stroke-width="3"/>
    <path d="M230 182 Q300 186 352 200" fill="none" stroke="#2f2f2f" stroke-width="3"/>
  </svg>
  <h2 class="abs center testi-title">CLIENT <span>TESTIMONIALS</span></h2>
  <p class="abs quote">Our partnership with Lumen Tech Guild has helped Northwind better understand the needs of the SMB IT market and to showcase our solutions to technical experts in a meaningful and engaging way.</p>
  <p class="abs cite">DANA ELLIS – NATIONAL SALES MANAGER<br>NORTHWIND SYSTEMS LIMITED</p>
  <div class="abs testi-nav"><span>‹</span><span>›</span></div>
  <div class="abs portrait" role="img" aria-label="Portrait of the quoted client in a dark suit"></div>
  <div class="abs mark mark--foot"><i></i></div>

  <div class="abs foot-brand"><span class="brand-dot"></span><span class="brand-name">LUMEN<br>TECH GUILD</span></div>
  <div class="abs social"><i></i><i></i><i></i><i></i><i></i></div>
  <h4 class="abs foot-h" style="left:118px;top:993px">QUICK LINKS</h4>
  <div class="abs links"><span>How It Works</span><span>Media</span><span>Join</span><span>Events</span><span>Chapters</span><span>Shop</span><span>Members</span><span>About Us</span><span>Partners</span><span>Strength</span></div>
  <h4 class="abs foot-h" style="left:200px;top:993px">JOIN US.</h4>
  <p class="abs join-text">Sed ut perspiciatis unde omnis iste natus error sit voluptatem</p>
  <div class="abs signup">Enter Email<b>SIGN UP</b></div>
  <div class="abs foot-rule"></div>
  <p class="abs center copy">© Copyright 2020. Lumen Tech Guild Limited. All rights reserved.</p>
</section>

<!-- ===== Dark theme ===== -->
<section class="page page--dark">
  <div class="abs header"></div>
  <div class="abs callbar"><svg viewBox="0 0 10 10"><circle cx="5" cy="5" r="4.3" fill="none" stroke="#fff" stroke-width=".8"/><path d="M3.4 2.8l1 .9-.5.7a3 3 0 0 0 1.7 1.7l.7-.5.9 1-.6.7C4.6 7.1 2.9 5.4 2.7 3.4z" fill="#fff"/></svg>CALL US : 1 800 555 0199</div>
  <nav class="abs nav"><span class="active">HOME</span><span>HOW IT WORKS</span><span>JOIN</span><span>CHAPTERS</span><span>MEMBERS</span><span>PARTNERS</span><span>MORE</span></nav>
  <div class="abs brand"><span class="brand-dot"></span><span class="brand-name">LUMEN<br>TECH GUILD</span></div>

  <div class="abs hero-photo" role="img" aria-label="Smiling young professional in a suit in a bright office"></div>
  <h1 class="abs hero-title">STRENGTH<br>IN <span>NUMBERS</span></h1>
  <p class="abs hero-sub">Sed ut perspiciatis unde omnis iste natus voluptatem</p>
  <div class="abs btns">
    <span class="btn">JOIN US <svg viewBox="0 0 10 10"><circle cx="5" cy="5" r="4.2" fill="none" stroke="#fff" stroke-width=".8"/><path d="M3 5h4M5.4 3.4 7 5 5.4 6.6" fill="none" stroke="#fff" stroke-width=".8"/></svg></span>
    <span class="btn btn--dark">DOWNLOAD BROCHURE <svg viewBox="0 0 10 10"><circle cx="5" cy="5" r="4.2" fill="none" stroke="#fff" stroke-width=".8"/><path d="M3 5h4M5.4 3.4 7 5 5.4 6.6" fill="none" stroke="#fff" stroke-width=".8"/></svg></span>
  </div>
  <div class="abs dots"><i></i><i></i><i class="on"></i><i></i><i></i></div>
  <div class="abs side" style="top:112px"><span class="side-tab"><b></b></span></div>
  <div class="abs side" style="top:127px"><span class="side-join"><b></b>JOIN US</span></div>
  <div class="abs side" style="top:143px"><span class="side-tab"><b></b></span></div>
  <svg class="abs hero-wave" viewBox="0 0 352 45" preserveAspectRatio="none">
    <path d="M0 27 Q170 40 352 14 L352 45 L0 45Z" fill="var(--bg)"/>
    <path d="M0 26 Q120 44 250 24" fill="none" stroke="var(--orange)" stroke-width="4"/>
    <path d="M190 16 Q290 6 352 20" fill="none" stroke="#444" stroke-width="4"/>
  </svg>
  <div class="abs mark"><i></i></div>

  <h2 class="abs center h2" style="top:263px">GROW YOUR BUSINESS,<br><em>GROW YOUR REPUTATION</em></h2>
  <div class="abs intro">
    <p>Lumen Tech Guild is Australia's leading industry association for IT business owners and professionals specialising in IT solutions for small and medium business.</p>
    <p>As a Lumen Tech Guild member you can draw upon, and add to, the collective knowledge bank of best-practice solutions and expert opinions garnered from a national network of IT business owners and professionals.</p>
  </div>

  <div class="abs alt-band"></div>
  <svg class="abs swoosh" viewBox="0 0 352 330" preserveAspectRatio="none">
    <path d="M300 75 Q330 62 352 55 L352 61 Q330 68 300 80Z" fill="var(--orange)"/>
    <path d="M0 280 Q20 268 71 258 L71 262 Q25 272 0 287Z" fill="var(--orange)"/>
  </svg>
  <div class="abs pillar" style="left:48px;top:364px;width:82px;height:82px">
    <svg viewBox="0 0 20 20" fill="none" stroke="#fff" stroke-width="1"><circle cx="8" cy="8" r="5.5"/><path d="M12 12l5 5"/></svg>
    <h3>Seek</h3><p>Liberate your time and find proven IT solutions fast via the Lumen Tech Guild Forum.</p>
  </div>
  <div class="abs pillar pillar--main" style="left:126px;top:356px;width:100px;height:100px">
    <svg viewBox="0 0 20 20" fill="none" stroke="#fff" stroke-width="1"><path d="M4 6h4a2 2 0 1 1 4 0h4v4a2 2 0 1 0 0 4v3H4v-3a2 2 0 1 0 0-4z"/></svg>
    <h3>Solve</h3><p>Create a more efficient and effective business, and deliver greater value to your customers via fast, effective problem-solving.</p>
  </div>
  <div class="abs pillar" style="left:222px;top:364px;width:82px;height:82px">
    <svg viewBox="0 0 20 20" fill="none" stroke="#fff" stroke-width=".9"><rect x="7" y="7" width="6" height="6"/><circle cx="10" cy="2.5" r="1.3"/><circle cx="10" cy="17.5" r="1.3"/><circle cx="2.5" cy="10" r="1.3"/><circle cx="17.5" cy="10" r="1.3"/><path d="M10 4v3M10 13v3M4 10h3M13 10h3"/></svg>
    <h3>Share</h3><p>Join the collective buying power and influence of Australia's largest industry association for small &amp; medium business IT.</p>
  </div>

  <h2 class="abs center h2" style="top:482px">FIND YOUR LOCAL<br><em>LUMEN TECH GUILD CHAPTER.</em></h2>
  <span class="abs btn find-btn">FIND NOW <svg viewBox="0 0 10 10"><circle cx="5" cy="5" r="4.2" fill="none" stroke="#fff" stroke-width=".8"/><path d="M3 5h4M5.4 3.4 7 5 5.4 6.6" fill="none" stroke="#fff" stroke-width=".8"/></svg></span>
  <div class="abs video" role="img" aria-label="Video still of a presenter speaking on a city street"></div>
  <svg class="abs play" viewBox="0 0 20 20"><circle cx="10" cy="10" r="9" fill="rgba(0,0,0,.35)" stroke="#fff" stroke-width="1"/><path d="M8 6l6 4-6 4z" fill="#fff"/></svg>

  <h2 class="abs center h2" style="top:698px">KEY <em>PARTNERS</em></h2>
  <div class="abs logos">
    <span class="arrow">‹</span>
    <span class="badge"><i></i></span><span class="badge"><i></i></span><span class="badge"><i></i></span><span class="badge"><i></i></span><span class="badge"><i></i></span>
    <span class="arrow">›</span>
  </div>

  <svg class="abs orange-wave" viewBox="0 0 352 220" preserveAspectRatio="none">
    <path d="M0 28 Q90 36 170 30 Q270 16 352 20 L352 204 Q250 170 170 186 Q80 206 0 196Z" fill="var(--orange)"/>
    <path d="M0 26 Q50 40 130 38" fill="none" stroke="#222" stroke-width="3"/>
    <path d="M230 182 Q300 186 352 200" fill="none" stroke="#222" stroke-width="3"/>
  </svg>
  <h2 class="abs center testi-title">CLIENT <span>TESTIMONIALS</span></h2>
  <p class="abs quote">Our partnership with Lumen Tech Guild has helped Northwind better understand the needs of the SMB IT market and to showcase our solutions to technical experts in a meaningful and engaging way.</p>
  <p class="abs cite">DANA ELLIS – NATIONAL SALES MANAGER<br>NORTHWIND SYSTEMS LIMITED</p>
  <div class="abs testi-nav"><span>‹</span><span>›</span></div>
  <div class="abs portrait" role="img" aria-label="Portrait of the quoted client in a dark suit"></div>
  <div class="abs mark mark--foot"><i></i></div>

  <div class="abs foot-brand"><span class="brand-dot"></span><span class="brand-name">LUMEN<br>TECH GUILD</span></div>
  <div class="abs social"><i></i><i></i><i></i><i></i><i></i></div>
  <h4 class="abs foot-h" style="left:118px;top:993px">QUICK LINKS</h4>
  <div class="abs links"><span>How It Works</span><span>Media</span><span>Join</span><span>Events</span><span>Chapters</span><span>Shop</span><span>Members</span><span>About Us</span><span>Partners</span><span>Strength</span></div>
  <h4 class="abs foot-h" style="left:200px;top:993px">JOIN US.</h4>
  <p class="abs join-text">Sed ut perspiciatis unde omnis iste natus error sit voluptatem</p>
  <div class="abs signup">Enter Email<b>SIGN UP</b></div>
  <div class="abs foot-rule"></div>
  <p class="abs center copy">© Copyright 2020. Lumen Tech Guild Limited. All rights reserved.</p>
</section>

</body>
</html>
```